Torvane PT Business Card

I need the card to be bright/bold colours to stand out amongst others.
It needs to have my company logo.
I was not interested in pictures etc just a layout that attracts attention.

I have attached my old design which is very plain. I also needed change the contact details. And my description changed to Personal Trainer
Phone 0427391058
Facebook Torvane PT
No email address please, no street address.
And only Torvane PT (Please remove anything to do with Torvane Supplements)

```html
<!DOCTYPE html>
<html lang="en">
<head>
<meta charset="utf-8">
<title>Torvane PT Business Card</title>
<link rel="stylesheet" href="https://fonts.googleapis.com/css2?family=Questrial&family=Arimo:wght@400;700&family=Montserrat:wght@800&display=swap">
<style>
  :root {
    --stage: #2e2e2e;
    --paper: #f6f6f4;
    --rule: #7d8a94;
    --blue-edge: #1786cc;
    --blue-glow: #3db4ea;
    --brand-blue: #1d8fd8;
    --icon-green: #5fb52f;
    --band-green: #9ccd3a;
    --gold-edge: #c9a516;
    --gold-glow: #fde214;
    --white: #ffffff;
    --title: #6a5a2a;
  }
  * { box-sizing: border-box; margin: 0; padding: 0; }
  html, body { width: 1200px; height: 800px; overflow: hidden; }
  body { background: var(--stage); position: relative; font-family: "Questrial", sans-serif; }

  .card {
    position: absolute; top: 243px; width: 553px; height: 315px;
    overflow: hidden; box-shadow: 0 6px 18px rgba(0,0,0,.45);
  }
  .card--green { left: 35px; }
  .card--gold { left: 611px; }

  .card__head { position: absolute; inset: 0 0 auto 0; height: 109px; background: var(--paper); }
  .card__body {
    position: absolute; top: 109px; left: 0; right: 0; height: 166px;
    background: radial-gradient(ellipse 60% 90% at 45% 40%, var(--blue-glow), var(--blue-edge));
    border-top: 2px solid var(--rule);
  }
  .card__notch { position: absolute; top: 107px; left: 30px; width: 30px; height: 12px; }
  .card__foot { position: absolute; left: 0; right: 0; bottom: 0; height: 40px; border-top: 2px solid rgba(255,255,255,.7); }
  .card--green .card__foot { background: var(--band-green); }
  .card--gold .card__foot { background: linear-gradient(90deg, var(--gold-edge), var(--gold-glow) 55%, var(--gold-edge)); }

  .brand { position: absolute; left: 39px; top: 50px; display: flex; align-items: center; gap: 8px; }
  .brand__mark { width: 14px; height: 14px; border-radius: 50%; background: var(--brand-blue); }
  .brand__name {
    font-family: "Montserrat", sans-serif; font-weight: 800; font-size: 30px;
    letter-spacing: 1px; color: var(--brand-blue); line-height: 1;
  }

  .contacts { position: absolute; left: 28px; top: 119px; list-style: none; }
  .contacts li { display: flex; align-items: center; gap: 6px; height: 34px; color: var(--white); font-size: 13.5px; letter-spacing: .3px; }
  .contacts svg { width: 23px; height: 23px; flex: none; }

  .person { position: absolute; right: 32px; top: 135px; text-align: right; }
  .person__name { font-family: "Arimo", sans-serif; font-weight: 700; font-size: 24px; color: var(--white); line-height: 1; }
  .person__role { font-family: "Arimo", sans-serif; font-weight: 400; font-size: 16px; color: var(--title); line-height: 1.2; margin-top: 2px; }
</style>
</head>
<body>

<svg width="0" height="0" style="position:absolute">
  <defs>
    <g id="icon-ring"><circle cx="12" cy="12" r="11" fill="#fff"/><circle cx="12" cy="12" r="9.3" fill="#5fb52f"/></g>
    <symbol id="icon-phone" viewBox="0 0 24 24"><use href="#icon-ring"/><path d="M8.6 6.5l1.8 2.3-1 1.2c.6 1.6 1.8 2.9 3.5 3.6l1.2-1 2.3 1.7-1 1.9c-3.6.1-7.9-4.1-7.8-7.9z" fill="#fff"/></symbol>
    <symbol id="icon-social" viewBox="0 0 24 24"><use href="#icon-ring"/></symbol>
  </defs>
</svg>

<article class="card card--green">
  <div class="card__head"></div>
  <div class="card__body"></div>
  <svg class="card__notch" viewBox="0 0 30 12"><path d="M0 2h7l8 9 8-9h7" fill="#f6f6f4" stroke="#7d8a94" stroke-width="2"/></svg>
  <div class="card__foot"></div>
  <div class="brand"><span class="brand__name">TORVANE PT</span><span class="brand__mark"></span></div>
  <ul class="contacts">
    <li><svg><use href="#icon-phone"/></svg>0427391058</li>
    <li><svg><use href="#icon-social"/></svg>Torvane PT</li>
  </ul>
  <div class="person"><p class="person__name">Sam Hartley</p><p class="person__role">Personal Trainer</p></div>
</article>

<article class="card card--gold">
  <div class="card__head"></div>
  <div class="card__body"></div>
  <svg class="card__notch" viewBox="0 0 30 12"><path d="M0 2h7l8 9 8-9h7" fill="#f6f6f4" stroke="#7d8a94" stroke-width="2"/></svg>
  <div class="card__foot"></div>
  <div class="brand"><span class="brand__name">TORVANE PT</span><span class="brand__mark"></span></div>
  <ul class="contacts">
    <li><svg><use href="#icon-phone"/></svg>0427391058</li>
    <li><svg><use href="#icon-social"/></svg>Torvane PT</li>
  </ul>
  <div class="person"><p class="person__name">Sam Hartley</p><p class="person__role">Personal Trainer</p></div>
</article>

</body>
</html>
```